Clean professional design needed for landscape property business

We need a logo for a new lawncare, landscaping , property maintenance business called Meadow Trim.
Our services include lawn mowing, garden maintenance, clean ups and some property maintenance.
We want a double sided business card that is clean and very professional using the colour scheme from our logo which is provided.
the business card should have impact as we will use these to drop into people's letterboxes as a marketing drop.
Initially we want to see what you come up with so there is a very wide scope here to work with.
Updates

Project Deadline Extended
Reason: we feel our original deadline was too short. we have extended to give more time for quality submissions.

Target Market(s)

High end property owners who don't wish to do there own gardneing or property maintenance

Industry/Entity Type

Business

Contact Information for Business Card

Name
Postion/ Title
Phone number
mobile
web address
physical address

services offered

Font styles to use
Sans Serif

Requirements
Must have
• curved edges preferrred
Nice to have
• We like the idea of the logo being embossed or etched into the card so it looks like it is below the surface of the card
Should not have
• No stock images or characters.

```html
<!DOCTYPE html>
<html lang="en">
<head>
<meta charset="utf-8">
<title>Meadow Trim – Business Card</title>
<link rel="stylesheet" href="https://fonts.googleapis.com/css2?family=Open+Sans:wght@400;600;700&display=swap">
<style>
  :root {
    --backdrop: #e4e5e6;
    --card-dark: #58595b;
    --card-dark-edge: #4d4e50;
    --etched: #4a4b4d;
    --etched-light: #646567;
    --card-light: #ffffff;
    --card-light-shade: #f1f1f1;
    --green: #7ab51d;
    --ink: #222222;
    --ink-soft: #333333;
  }
  * { box-sizing: border-box; margin: 0; padding: 0; }
  html, body {
    width: 1200px; height: 864px; overflow: hidden;
    background: var(--backdrop);
    font-family: "Open Sans", Arial, sans-serif;
  }
  .canvas { position: relative; width: 1200px; height: 864px; }

  .card {
    position: absolute;
    width: 560px; height: 320px;
    border-radius: 12px;
    overflow: hidden;
    box-shadow: 0 6px 18px rgba(0,0,0,.18);
  }

  /* Back side */
  .card-back {
    left: 200px; top: 80px;
    background: var(--card-dark);
  }
  .card-back .brand-etched {
    position: absolute; left: 70px; top: 34px;
    display: flex; align-items: center; gap: 14px;
    font-weight: 700; font-size: 46px; letter-spacing: -1px;
    color: var(--etched);
    text-shadow: 0 1px 0 var(--etched-light);
  }
  .brand-etched .brand-square {
    width: 22px; height: 22px; background: var(--etched);
  }
  .services {
    position: absolute; left: 0; right: 0; top: 150px;
    text-align: center;
  }
  .services-title {
    color: var(--green); font-weight: 600; font-size: 15px;
    letter-spacing: .3px; margin-bottom: 10px;
  }
  .services-list { list-style: none; color: #ffffff; font-size: 15px; line-height: 1.35; }
  .services-list li::before {
    content: ""; display: inline-block;
    width: 7px; height: 7px; background: var(--green);
    margin-right: 8px; vertical-align: 2px;
  }

  /* Front side */
  .card-front {
    left: 440px; top: 470px;
    background: linear-gradient(135deg, var(--card-light) 40%, var(--card-light-shade) 100%);
  }
  .brand {
    position: absolute; right: 40px; top: 48px;
    display: flex; align-items: center; gap: 12px;
    font-weight: 700; font-size: 38px; letter-spacing: -1px;
    color: var(--green);
  }
  .brand .brand-square { width: 18px; height: 18px; background: var(--green); }
  .person { position: absolute; left: 40px; top: 112px; }
  .person-name { color: var(--green); font-weight: 600; font-size: 18px; line-height: 1.2; }
  .person-role { color: var(--ink); font-size: 12px; }
  .divider {
    position: absolute; left: 0; right: 0; top: 162px;
    height: 1.5px; background: var(--green);
  }
  .contacts {
    position: absolute; right: 30px; top: 196px;
    list-style: none; text-align: right;
    color: var(--ink-soft); font-size: 14px; line-height: 1.55;
  }
  .contacts li { display: flex; justify-content: flex-end; align-items: center; gap: 10px; }
  .contacts .icon { width: 12px; height: 12px; flex: none; }
  .contacts .icon-spacer { width: 12px; flex: none; }
</style>
</head>
<body>
<main class="canvas">

  <section class="card card-back" aria-label="Business card, back">
    <div class="brand-etched">Meadow Trim <span class="brand-square"></span></div>
    <div class="services">
      <h2 class="services-title">SERVICES OFFERED</h2>
      <ul class="services-list">
        <li>Lawn Mowing</li>
        <li>Garden Maintenance</li>
        <li>Clean Ups</li>
        <li>Property Maintenance</li>
      </ul>
    </div>
  </section>

  <section class="card card-front" aria-label="Business card, front">
    <div class="brand">Meadow Trim <span class="brand-square"></span></div>
    <div class="person">
      <p class="person-name">Sam Carter</p>
      <p class="person-role">Project Manager</p>
    </div>
    <div class="divider"></div>
    <ul class="contacts">
      <li>123 456 7890
        <svg class="icon" viewBox="0 0 24 24" aria-hidden="true"><path fill="#7ab51d" d="M6.6 10.8a15 15 0 0 0 6.6 6.6l2.2-2.2c.3-.3.7-.4 1-.2 1.1.4 2.3.6 3.6.6.6 0 1 .4 1 1V20c0 .6-.4 1-1 1A17 17 0 0 1 3 4c0-.6.4-1 1-1h3.5c.6 0 1 .4 1 1 0 1.3.2 2.5.6 3.6.1.3 0 .7-.2 1z"/></svg>
      </li>
      <li>sam@meadowtrim.com
        <svg class="icon" viewBox="0 0 24 24" aria-hidden="true"><rect x="2" y="5" width="20" height="14" rx="1.5" fill="#7ab51d"/><path d="M3 6l9 7 9-7" fill="none" stroke="#fff" stroke-width="1.6"/></svg>
      </li>
      <li>www.meadowtrim.com
        <svg class="icon" viewBox="0 0 24 24" aria-hidden="true"><circle cx="12" cy="12" r="10" fill="#7ab51d"/><path d="M2 12h20M12 2c3 3 3 17 0 20M12 2c-3 3-3 17 0 20" fill="none" stroke="#fff" stroke-width="1.4"/></svg>
      </li>
      <li>Address Line1, Address Line2, country -123456 <span class="icon-spacer"></span></li>
    </ul>
  </section>

</main>
</body>
</html>
```